Audio Visual Services Brochure for Direct Mailing

We are looking to design a direct mailing brochure detailing a new product that we are hoping to install in our immediate surrounding areas in London, UK. We are hoping for a half fold design, with a front page, two page centre spread and a rear page.
We have some very specific information that we want in the middle spread and want to tie this in for the front and rear pages.

Front Page Brief;
This page needs to deliver a problem that most modern households have in that they have too many remote controls (TV, DVD/Bluray, AV Reciever, Satellite TV, Plimmo TV, etc. etc.) We have taken a photo of this situation which may need to be improvded on.
We were hoping to design a page that presents this issue with text that backs up the photo along the lines of, "Does this look familiar? Too many remote controls and a complicated television system?". This page needs to grab the customer if they have this issue.

Centre Spread Brief;
This page presents two solutions to the first pages problem, A single room solution all in one remote control and a whole house solution which details how the system can scale to include lighting, multi-room audio distribution, cctv & security integration, HD/4K video distribution offering all of your video sources on all TV's in the property, Door entry, intercoms etc. etc.
This centre page has been taken from the manufacturers brochure and wants to be kept almost as is. We are very happy with this layout already.

Rear Page Brief;
Here we are hoping to provide a next step / contact us type of page with our company details, perhaps providing some company values and definitely pushing that we have been a SW20 local AV systems specialist since 2004.

Our website is at http://www.halvane-homeworks.co.uk which unfortunately still has our old company logo on it but this should help with services etc.

Any other questions please don't hesitate to get in contact.

Target Market(s)

Residential End User Homes - Mid to high income earners that can afford a £1K to £3K remote control system.

Industry/Entity Type

Audio

Font styles to use
Sans Serif

Colors

Designer to choose colors to be used in the design.

Requirements
Must have
• A catchy first page that entices the reader to open the brochure to see the middle section. Front page must be an attention grabber

```html
<!DOCTYPE html>
<html lang="en">
<head>
<meta charset="utf-8">
<title>Halvane Homeworks – Brochure Spread</title>
<link href="https://fonts.googleapis.com/css2?family=Oswald:wght@300;400;500&family=Montserrat:wght@700;800&family=Open+Sans:wght@400;600;700&display=swap" rel="stylesheet">
<style>
  :root{
    --navy:#03264b;
    --brand-blue:#0b3c6e;
    --band-blue:#0c4677;
    --ink:#333333;
    --panel-grey:#505050;
    --white:#ffffff;
    --strip-grey:#6a6a6a;
  }
  *{margin:0;padding:0;box-sizing:border-box}
  html,body{width:1200px;height:1200px;overflow:hidden;background:var(--navy)}
  .spread{
    position:absolute;left:40px;top:201px;width:1097px;height:782px;
    transform:scale(1.021);transform-origin:0 0;
    box-shadow:0 20px 50px rgba(0,0,0,.45);
    font-family:"Open Sans",sans-serif;
  }
  .page{position:absolute;top:0;width:548px;height:782px;overflow:hidden}
  .page--rear{left:0;background:var(--panel-grey)}
  .page--front{left:548px;background:var(--white)}
  .page svg.art{position:absolute;left:0;top:0;width:548px;height:782px}

  /* rear page */
  .rear-brand{position:absolute;top:400px;left:0;width:548px;text-align:center;
    font-weight:700;font-size:30px;letter-spacing:2px;color:var(--white)}
  .rear-company{position:absolute;top:471px;left:0;width:548px;text-align:center;
    font-weight:600;font-size:14px;color:var(--white)}
  .contact{position:absolute;top:514px;left:0;width:548px;text-align:center;
    font-size:12.5px;line-height:17.5px;color:#eeeeee;list-style:none}
  .contact li{display:flex;justify-content:center;align-items:center;gap:7px}
  .contact li.plain{gap:0}
  .contact li.gap{margin-top:4px}
  .contact svg{width:12px;height:12px;flex:none}
  .since-pill{position:absolute;left:38px;top:688px;width:473px;height:43px;border-radius:22px;
    background:var(--white);color:#222;font-weight:600;font-size:19px;
    display:flex;align-items:center;justify-content:center}

  /* front page */
  .headline{position:absolute;left:0;width:548px;text-align:center}
  .headline--kicker{top:30px;font-family:"Oswald",sans-serif;font-weight:400;font-size:44px;
    color:var(--brand-blue);transform:scaleX(.9)}
  .headline--main{top:76px;font-family:"Montserrat",sans-serif;font-weight:800;font-size:62px;
    color:var(--ink);letter-spacing:1px}
  .problem{position:absolute;right:52px;top:512px;text-align:right;line-height:31px}
  .problem .soft{font-family:"Open Sans",sans-serif;font-weight:600;font-size:21px;color:var(--brand-blue)}
  .problem .firm{font-family:"Oswald",sans-serif;font-weight:500;font-size:23px;color:#111}
  .front-brand{position:absolute;left:55px;top:648px;font-weight:700;font-size:38px;
    letter-spacing:2px;color:var(--brand-blue)}
</style>
</head>
<body>
<div class="spread">

  <section class="page page--rear">
    <svg class="art" viewBox="0 0 548 782">
      <defs>
        <linearGradient id="photoGrey" x1="0" y1="0" x2="1" y2="1">
          <stop offset="0" stop-color="#d9d9d9"/>
          <stop offset=".5" stop-color="#8a8a8a"/>
          <stop offset="1" stop-color="#3a3a3a"/>
        </linearGradient>
        <radialGradient id="panelGlow" cx=".5" cy=".35" r=".7">
          <stop offset="0" stop-color="#666666"/>
          <stop offset="1" stop-color="#3c3c3c"/>
        </radialGradient>
        <linearGradient id="stripBlue" x1="0" x2="1">
          <stop offset="0" stop-color="#0b3a66"/>
          <stop offset=".5" stop-color="#14578a"/>
          <stop offset="1" stop-color="#0b3a66"/>
        </linearGradient>
      </defs>
      <rect width="548" height="782" fill="url(#panelGlow)"/>
      <rect role="img" aria-label="Black and white photo of a hand using a touch control tablet beside a remote" x="0" y="0" width="548" height="470" fill="url(#photoGrey)"/>
      <path d="M0 375 C120 300 300 285 400 320 C470 345 520 395 548 445 L548 782 L0 782 Z" fill="var(--band-blue)"/>
      <path d="M0 485 C130 370 320 330 440 360 C490 375 525 410 548 445 L548 782 L0 782 Z" fill="var(--white)"/>
      <path d="M0 495 C130 385 320 345 430 370 C485 385 522 415 548 452 L548 782 L0 782 Z" fill="url(#panelGlow)"/>
      <rect x="0" y="756" width="548" height="26" fill="url(#stripBlue)"/>
    </svg>
    <div class="rear-brand">HALVANE</div>
    <div class="rear-company">Halvane Homeworks Limited</div>
    <ul class="contact">
      <li><svg viewBox="0 0 12 12"><path d="M6 1a3 3 0 0 0-3 3c0 2.3 3 6 3 6s3-3.7 3-6a3 3 0 0 0-3-3z" fill="none" stroke="#fff" stroke-width="1.2"/><circle cx="6" cy="4" r="1" fill="#fff"/><path d="M2 11h8" stroke="#fff"/></svg>Larkfield House</li>
      <li class="plain">418 Merrow Road</li>
      <li class="plain">Raynes Park ,SW20 0QT</li>
      <li class="gap"><svg viewBox="0 0 12 12"><path d="M3 1l2 2.5-1.2 1.3a7 7 0 0 0 3.4 3.4L8.5 7 11 9l-1.5 2C5 11 1 7 1 2.5z" fill="#fff"/></svg>01632 960 410</li>
      <li class="gap"><svg viewBox="0 0 12 12"><rect x="3" y="1" width="6" height="3" fill="none" stroke="#fff"/><rect x="1" y="4" width="10" height="5" rx="1" fill="none" stroke="#fff"/><rect x="3" y="7" width="6" height="4" fill="none" stroke="#fff"/></svg>01632 960 411</li>
      <li class="gap"><svg viewBox="0 0 12 12"><rect x="1" y="2.5" width="10" height="7" fill="none" stroke="#fff"/><path d="M1 2.5l5 4 5-4" fill="none" stroke="#fff"/></svg>sales@halvane-homeworks.co.uk</li>
      <li class="gap"><svg viewBox="0 0 12 12"><circle cx="6" cy="6" r="5" fill="none" stroke="#fff"/><ellipse cx="6" cy="6" rx="2.2" ry="5" fill="none" stroke="#fff"/><path d="M1 6h10" stroke="#fff"/></svg>www.halvane-homeworks.co.uk</li>
    </ul>
    <div class="since-pill">SW20 local AV systems specialist since 2004</div>
  </section>

  <section class="page page--front">
    <svg class="art" viewBox="0 0 548 782">
      <defs>
        <linearGradient id="photoWarm" x1="0" y1="0" x2="1" y2="1">
          <stop offset="0" stop-color="#c9a58a"/>
          <stop offset=".45" stop-color="#5a4a44"/>
          <stop offset="1" stop-color="#b88b6e"/>
        </linearGradient>
      </defs>
      <path role="img" aria-label="Photo of hands holding a stack of many TV remote controls over a knitted jumper"
        d="M0 176 H548 V722 C440 722 330 700 230 645 C140 595 80 530 30 462 L0 430 Z" fill="url(#photoWarm)"/>
      <path class="text-field" d="M548 510 C430 505 300 540 200 600 L200 782 H548 Z" fill="var(--white)"/>
      <path class="swoosh" d="M30 462 C110 540 220 610 340 655 C430 680 500 686 548 686 V722 C440 722 330 700 230 645 C140 595 80 530 30 462 Z" fill="var(--band-blue)"/>
      <rect x="0" y="756" width="548" height="26" fill="var(--strip-grey)"/>
    </svg>
    <div class="headline headline--kicker">DOES THIS LOOK</div>
    <div class="headline headline--main">FAMILIAR?</div>
    <div class="problem">
      <div class="soft">Too Many</div>
      <div class="soft">Remote Controls &amp;</div>
      <div class="firm">A Complicated</div>
      <div class="firm">Television System?</div>
    </div>
    <div class="front-brand">HALVANE</div>
  </section>

</div>
</body>
</html>
```